Create a Eye Catching Flyerr for my online business

I would like an eye catching flyer with the relevant content for my business.

This flyer is to advertise my online business and the call to action is to get Butchers to sign up to my online site to start selling their products.

the flyer must be eye catching, each to understand, easy to read and relevant to the audience being local butcher shops.

Attached is the marketing packs with all the required information about the business The flyer must not be too long, but the front page must be catching and want the audience to read more. It must very direct, targeted and focused on the audience

It mus be duplicate sides

Reason: need a little more time for review

Industry/Entity Type

Marketing

Font styles to use
Serif
Sans Serif

Colors
9bcb3b
ffffff
fee18a
fac994
f37122
f78f20
ffc214

```html
<!DOCTYPE html>
<html lang="en">
<head>
<meta charset="utf-8">
<title>Click that Clicked – Harbour &amp; Hoof two-sided flyer</title>
<link rel="stylesheet" href="https://fonts.googleapis.com/css2?family=Bowlby+One+SC&family=Fredoka:wght@500;600&family=Poppins:wght@400;600;700;800&display=swap">
<style>
  :root {
    --orange: #f37122;
    --orange-light: #f78f20;
    --peach: #fac994;
    --cream: #fee18a;
    --gold: #ffc214;
    --green: #9bcb3b;
    --white: #ffffff;
    --ink: #1a1a1a;
    --meat: #a8292c;
  }
  html, body { margin: 0; padding: 0; overflow: hidden; background: var(--white); }
  .flyer {
    position: relative;
    width: 848px;
    height: 1200px;
    overflow: hidden;
    perspective: 2400px;
    font-family: "Poppins", sans-serif;
  }
  .flyer-sheet {
    position: absolute; inset: 0;
    transform-style: preserve-3d;
    transition: transform 0.9s ease;
  }
  .flyer:hover .flyer-sheet,
  .flyer:focus-within .flyer-sheet { transform: rotateY(180deg); }
  .side {
    position: absolute; inset: 0;
    background: var(--white);
    backface-visibility: hidden;
    overflow: hidden;
  }
  .side-back { transform: rotateY(180deg); }

  /* ---------- front side ---------- */
  .backdrop { position: absolute; inset: 0; }
  .headline { position: absolute; left: 0; top: 0; margin: 0; font-weight: normal; }
  .headline span { position: absolute; white-space: nowrap; line-height: 1; }
  .headline-click {
    left: 85px; top: 116px;
    font-weight: 800; font-size: 78px;
    color: var(--orange); letter-spacing: 1px;
  }
  .headline-that {
    left: 192px; top: 194px;
    font-weight: 400; font-size: 66px; color: var(--ink);
  }
  .headline-clicked {
    left: 250px; top: 284px;
    font-family: "Bowlby One SC", sans-serif;
    font-size: 102px; color: var(--meat); letter-spacing: 2px;
  }
  .brand {
    position: absolute; left: 598px; top: 24px; width: 230px;
    display: flex; flex-direction: column; align-items: center; gap: 10px;
  }
  .brand-dot { width: 120px; height: 120px; border-radius: 50%; background: var(--green); }
  .brand-name {
    font-weight: 700; font-size: 19px; color: var(--green);
    letter-spacing: 1px; text-transform: uppercase;
  }
  .chef-illustration {
    position: absolute; left: 389px; top: 447px; width: 397px; height: 268px;
    border-radius: 40px;
    background: radial-gradient(ellipse at 35% 40%, #ffffff 0%, #f6e3cf 45%, #f2b8a8 75%, #e98e86 100%);
  }
  .tagline-badge {
    position: absolute; left: 388px; top: 684px; width: 436px; height: 436px;
    border-radius: 50%; background: var(--white);
    display: flex; align-items: center; justify-content: center;
  }
  .tagline-badge p {
    margin: 0; width: 400px; height: 400px; border-radius: 50%;
    background: var(--peach); color: var(--orange);
    display: flex; align-items: center; justify-content: center; text-align: center;
    font-family: "Fredoka", sans-serif; font-weight: 500;
    font-size: 58px; line-height: 1.3;
  }
  .front-cta {
    position: absolute; left: 40px; top: 880px; width: 330px;
    color: var(--white);
  }
  .front-cta-lead { margin: 0 0 10px; font-weight: 800; font-size: 34px; line-height: 1.1; }
  .front-cta-body { margin: 0 0 18px; font-weight: 400; font-size: 20px; line-height: 1.4; }
  .front-cta-button {
    display: inline-block; padding: 10px 22px; border-radius: 30px;
    background: var(--white); color: var(--orange);
    font-weight: 700; font-size: 19px; text-decoration: none;
  }
  .site-link {
    position: absolute; left: 0; top: 1120px; width: 848px; height: 50px;
    display: flex; align-items: center; justify-content: center;
    font-weight: 600; font-size: 24px; color: var(--orange);
  }

  /* ---------- back side ---------- */
  .back-header {
    position: absolute; left: 0; top: 0; width: 848px; height: 330px;
    background: var(--orange); color: var(--white);
    box-sizing: border-box; padding: 70px 70px 0;
  }
  .back-kicker { margin: 0 0 12px; font-weight: 600; font-size: 22px; letter-spacing: 3px; text-transform: uppercase; color: var(--cream); }
  .back-title { margin: 0; font-weight: 800; font-size: 54px; line-height: 1.1; }
  .back-brand {
    position: absolute; right: 60px; top: 40px;
    display: flex; align-items: center; gap: 10px;
    font-weight: 700; font-size: 18px; color: var(--white); text-transform: uppercase; letter-spacing: 1px;
  }
  .back-brand-dot { width: 28px; height: 28px; border-radius: 50%; background: var(--green); }
  .benefits { position: absolute; left: 70px; top: 390px; width: 708px; margin: 0; padding: 0; list-style: none; }
  .benefit { display: flex; gap: 22px; align-items: flex-start; margin-bottom: 34px; }
  .benefit svg { flex: none; width: 46px; height: 46px; }
  .benefit-title { margin: 0 0 4px; font-weight: 700; font-size: 28px; color: var(--ink); }
  .benefit-text { margin: 0; font-weight: 400; font-size: 20px; line-height: 1.45; color: #444; }
  .back-cta {
    position: absolute; left: 70px; top: 930px; width: 708px; height: 150px;
    border-radius: 28px; background: var(--peach);
    display: flex; flex-direction: column; align-items: center; justify-content: center; gap: 6px;
  }
  .back-cta-title { margin: 0; font-family: "Fredoka", sans-serif; font-weight: 600; font-size: 44px; color: var(--orange); }
  .back-cta-text { margin: 0; font-weight: 600; font-size: 22px; color: var(--ink); }
  .back-band { position: absolute; left: 0; top: 1172px; width: 848px; height: 28px; background: var(--orange); }
</style>
</head>
<body>
<main class="flyer" tabindex="0">
  <div class="flyer-sheet">

    <section class="side side-front" aria-label="Front of flyer">
      <svg class="backdrop" width="848" height="1200" viewBox="0 0 848 1200" aria-hidden="true">
        <path d="M0 392 C60 600 200 760 420 800 C600 832 760 860 848 950 L848 1118 L0 1118 Z" fill="var(--orange)"/>
        <rect x="0" y="1172" width="848" height="28" fill="var(--orange)"/>
      </svg>

      <div class="brand">
        <span class="brand-dot"></span>
        <span class="brand-name">Harbour &amp; Hoof</span>
      </div>

      <h1 class="headline">
        <span class="headline-click">CLICK</span>
        <span class="headline-that">that</span>
        <span class="headline-clicked">CLICKED</span>
      </h1>

      <div class="chef-illustration" role="img" aria-label="Illustration of a cheerful chef making an okay gesture beside a leg of ham"></div>

      <div class="front-cta">
        <p class="front-cta-lead">Local butchers, sell online.</p>
        <p class="front-cta-body">List your cuts for free and reach new customers near your shop.</p>
        <a class="front-cta-button" href="#">Sign up today &rarr;</a>
      </div>

      <div class="tagline-badge">
        <p>Grow with<br>each click</p>
      </div>

      <div class="site-link">www.HarbourHoofMarket.com.au</div>
    </section>

    <section class="side side-back" aria-label="Back of flyer">
      <header class="back-header">
        <div class="back-brand"><span class="back-brand-dot"></span>Harbour &amp; Hoof</div>
        <p class="back-kicker">For local butcher shops</p>
        <h2 class="back-title">Your counter,<br>open online 24/7</h2>
      </header>

      <ul class="benefits">
        <li class="benefit">
          <svg viewBox="0 0 46 46" aria-hidden="true"><circle cx="23" cy="23" r="23" fill="var(--green)"/><path d="M13 24 l7 7 l13 -15" fill="none" stroke="var(--white)" stroke-width="4" stroke-linecap="round" stroke-linejoin="round"/></svg>
          <div><p class="benefit-title">Free to join</p><p class="benefit-text">Create your shop page in minutes. No setup fees, no lock-in.</p></div>
        </li>
        <li class="benefit">
          <svg viewBox="0 0 46 46" aria-hidden="true"><circle cx="23" cy="23" r="23" fill="var(--green)"/><path d="M13 24 l7 7 l13 -15" fill="none" stroke="var(--white)" stroke-width="4" stroke-linecap="round" stroke-linejoin="round"/></svg>
          <div><p class="benefit-title">Reach nearby buyers</p><p class="benefit-text">Shoppers in your area find your meat and fish by suburb.</p></div>
        </li>
        <li class="benefit">
          <svg viewBox="0 0 46 46" aria-hidden="true"><circle cx="23" cy="23" r="23" fill="var(--green)"/><path d="M13 24 l7 7 l13 -15" fill="none" stroke="var(--white)" stroke-width="4" stroke-linecap="round" stroke-linejoin="round"/></svg>
          <div><p class="benefit-title">You set the prices</p><p class="benefit-text">Update stock, specials and pick-up times whenever you like.</p></div>
        </li>
        <li class="benefit">
          <svg viewBox="0 0 46 46" aria-hidden="true"><circle cx="23" cy="23" r="23" fill="var(--green)"/><path d="M13 24 l7 7 l13 -15" fill="none" stroke="var(--white)" stroke-width="4" stroke-linecap="round" stroke-linejoin="round"/></svg>
          <div><p class="benefit-title">Paid fast</p><p class="benefit-text">Orders are paid online and settled straight to your account.</p></div>
        </li>
      </ul>

      <div class="back-cta">
        <p class="back-cta-title">Sign up your shop today</p>
        <p class="back-cta-text">www.HarbourHoofMarket.com.au</p>
      </div>

      <div class="back-band"></div>
    </section>

  </div>
</main>
</body>
</html>
```